依頼詳細
デザイン指示書を参考に居抜き物件をリフォームして開業を考えている人向けにデザインをしていただきたいと思います。
お客様の理想の店舗デザインを実現します。全体のイメージは、スタイリッシュでオシャレで、高級感のあるデザインを希望します。
サイトURL
ページ数
1ページ
希望イメージ
シンプル 複雑
単色 カラフル
暗い 明るい
日常 高級
遊び心 厳粛
未来的 伝統的
女性的 男性的
希望する色
茶系
納品ファイル
• 高解像度JPG (.jpg)
• イラストレーター形式 (.ai)
• フォトショップ形式 (.psd)
補足説明
レスポンシブデザインでお願い致します。指示書の中の事例画像は、現在準備中のため、ご提案をお願いします。
依頼金額を40000円に変更して、延長しました。
■ 選んだ理由

シンプルなデザインありがとうございました。

修正を引き続きよろしくお願いいたします。

■ 提案者全員のお礼・コメント

たくさんのデザインありがとうございました。
今後もデザインコンペを行ってまいりますのでよろしくお願い致します。

```html
<!DOCTYPE html>
<html lang="ja">
<head>
<meta charset="utf-8">
<title>店舗リフォームのミナト</title>
<link href="https://fonts.googleapis.com/css2?family=Noto+Sans+JP:wght@400;700&family=Noto+Serif+JP:wght@400;600&display=swap" rel="stylesheet">
<style>
:root{
  --ink:#2b2b2b;
  --muted:#777;
  --gold:#c9a36a;
  --dark:#2a1913;
  --brown:#3b1d14;
  --red:#d8574c;
  --blue:#3d6fa6;
  --navy:#1f2d4a;
  --green:#e3ebcd;
  --olive:#b9bf86;
  --line:#d8d8d8;
  --paper:#fff;
}
*{box-sizing:border-box;margin:0;padding:0}
html,body{width:1200px;height:3440px;overflow:hidden;background:var(--paper)}
body{font-family:"Noto Sans JP",sans-serif;color:var(--ink);position:relative}
.abs{position:absolute}
.serif{font-family:"Noto Serif JP",serif}
.ph{position:absolute}
/* header */
.header{left:0;top:0;width:1200px;height:48px}
.logo{left:120px;top:10px;font-size:18px;font-weight:700;color:var(--dark);display:flex;align-items:center;gap:8px}
.logo small{font-size:11px;font-weight:400}
.logo .name{font-size:26px;letter-spacing:2px}
.tel{right:120px;top:8px;display:flex;align-items:baseline;gap:10px;font-size:12px}
.tel b{font-size:30px;font-weight:400;font-family:"Noto Serif JP",serif}
.nav{left:0;top:48px;width:1200px;height:32px;background:var(--dark)}
.nav ul{list-style:none;display:flex;margin-left:120px;width:960px;height:32px}
.nav li{flex:1;color:#fff;font-size:13px;text-align:center;line-height:32px;border-right:1px solid #5a463e}
.nav li.on{background:var(--red)}
/* hero */
.hero{left:0;top:80px;width:1200px;height:460px;background:linear-gradient(135deg,#2a0b08 0%,#8d1d15 40%,#c8432e 65%,#3a120c 100%)}
.hero-copy{left:0;top:370px;color:#fff;font-size:36px;line-height:1.45;letter-spacing:3px}
.hero-copy span{display:inline-block;background:rgba(0,0,0,.45);padding:0 18px 0 30px;margin-bottom:6px}
.tag-after{left:920px;top:430px;width:210px;height:54px;background:#fff;color:var(--dark);font-size:34px;font-family:"Noto Serif JP",serif;text-align:center;line-height:54px}
.tag-before{left:1020px;top:484px;width:150px;height:40px;background:#5a4a44;color:#fff;font-size:22px;font-family:"Noto Serif JP",serif;text-align:center;line-height:40px}
/* headings */
.sec-head{left:72px;width:748px;display:flex;align-items:center;gap:14px;font-size:20px;border-bottom:1px solid var(--line);padding-bottom:10px}
.sec-head i{width:18px;height:18px;transform:rotate(45deg);display:block}
.sec-head em{font-style:normal;font-family:"Noto Serif JP",serif;font-size:24px}
.lead{left:72px;font-size:24px}
.para{font-size:12px;line-height:2;color:#444}
/* list */
.points{left:72px;top:1330px;width:400px;list-style:none}
.points li{display:flex;align-items:center;gap:22px;height:72px;border-bottom:1px solid var(--red);font-size:20px}
.points li b{font-family:"Noto Serif JP",serif;font-weight:400;font-size:38px;color:var(--red);width:36px}
/* works */
.work-cap{display:flex;align-items:center;justify-content:space-between;width:348px;border-bottom:1px solid var(--line);padding-bottom:6px}
.chip{background:var(--gold);color:#fff;font-size:11px;padding:3px 10px}
.work-cap span{font-size:18px;font-family:"Noto Serif JP",serif}
/* news */
.news{left:72px;top:3000px;list-style:none;font-size:13px}
.news li{display:flex;align-items:center;gap:26px;height:42px}
.news li i{width:12px;height:12px;background:var(--dark);transform:rotate(45deg);display:block}
/* sidebar */
.side{left:852px;width:280px}
.access{top:720px;height:280px;background:var(--navy);color:#fff;padding:16px 20px;text-align:center}
.access h3{font-weight:400;font-size:13px;letter-spacing:3px;border:1px solid #fff;padding:3px;margin-bottom:14px}
.access p{font-size:12px;line-height:1.7;text-align:left}
.access .big{font-size:15px;font-weight:700;margin-bottom:8px}
.access .ph-num{font-size:30px;font-family:"Noto Serif JP",serif;text-align:center;margin-top:6px}
.side-h{height:30px;color:#fff;font-size:13px;line-height:30px;padding-left:14px}
.case-list{list-style:none;background:var(--green);padding:8px 14px}
.case-list li{display:flex;align-items:center;gap:14px;height:50px;font-size:11px;border-bottom:1px dashed #b7c29a}
.case-list li div{width:58px;height:40px;background:linear-gradient(135deg,#5a3120,#c98a4e)}
.news-side li{display:flex;gap:12px;height:120px;padding:12px 0;font-size:11px;border-bottom:1px solid var(--line)}
.news-side li div{width:110px;height:84px;background:linear-gradient(135deg,#d9d9d9,#f3f3f3);border:1px solid #ccc;flex:none}
.badge{height:34px;border:1px solid #ccc;background:#f2f2f2}
/* footer */
.pagetop{left:1060px;top:3100px;font-size:12px;letter-spacing:1px}
.footer{left:0;top:3160px;width:1200px;height:280px;background:var(--brown)}
.fnav{left:120px;top:3372px;display:flex;gap:40px;color:#fff;font-size:12px}
.flogo{left:870px;top:3280px;color:#fff}
.flogo .n{font-size:20px;font-weight:700;display:flex;align-items:center;gap:8px}
.flogo .n b{font-size:26px;letter-spacing:2px}
.flogo p{font-size:11px;line-height:1.7;margin-top:4px}
.flogo .box{border:1px solid #fff;display:inline-block;padding:2px 8px;font-size:11px;margin-top:6px}
.flogo .num{font-size:28px;font-family:"Noto Serif JP",serif;margin-top:8px;background:#fff;color:var(--brown);padding:0 10px;display:inline-block}
</style>
</head>
<body>

<header class="abs header">
  <div class="abs logo"><small>店舗リフォームの</small><span class="name">ミナト</span></div>
  <div class="abs tel">お問い合わせは <b>028-000-4172</b></div>
</header>
<nav class="abs nav"><ul>
  <li class="on">HOME</li><li>リフォームとは</li><li>リフォーム工程</li><li>事例紹介</li><li>会社概要</li><li>お問合せ</li>
</ul></nav>

<section class="abs hero" role="img" aria-label="赤い照明の和風レストラン店内写真（リフォーム後）"></section>
<div class="abs hero-copy serif"><span>理想の店舗に</span><br><span>リフォームいたします</span></div>
<div class="abs tag-after">After</div>
<div class="abs tag-before">Before</div>

<!-- commitment -->
<h2 class="abs sec-head" style="top:720px"><i style="background:var(--gold)"></i>店舗リフォーム ✕ <em style="color:var(--gold)">こだわり</em></h2>
<p class="abs lead serif" style="top:800px">理想を現実にする極限までのこだわり</p>
<div class="ph" style="left:72px;top:868px;width:240px;height:150px;background:linear-gradient(135deg,#6b3a22,#d9a770)" role="img" aria-label="カウンター席のある店内写真"></div>
<div class="ph" style="left:326px;top:868px;width:240px;height:150px;background:linear-gradient(135deg,#8a6a4c,#e6d6bd)" role="img" aria-label="明るいカフェの店内写真"></div>
<div class="ph" style="left:580px;top:868px;width:240px;height:150px;background:linear-gradient(135deg,#4a2a1a,#b97a47)" role="img" aria-label="木目調のダイニング写真"></div>
<p class="abs para" style="left:72px;top:1040px;width:748px">お客様のご要望を丁寧にお伺いし、店舗の雰囲気や動線まで細かく考えたデザインをご提案します。素材選びから照明計画、家具の配置まで、一つひとつにこだわり抜いた空間づくりを行います。居抜き物件の良さを活かしながら、新しいお店の個性がしっかりと伝わる内装へ仕上げます。開業までのスケジュールやご予算にも柔軟に対応いたしますので、まずはお気軽にご相談ください。</p>

<!-- points -->
<h2 class="abs sec-head" style="top:1228px"><i style="background:var(--red)"></i>店舗リフォーム ✕ <em style="color:var(--red)">注意点</em></h2>
<ol class="abs points serif">
  <li><b>1.</b>予算を整理する</li>
  <li><b>2.</b>建物の状態を確認する</li>
  <li><b>3.</b>予算を整理する</li>
  <li><b>4.</b>建物の状態を確認する</li>
</ol>
<div class="ph" style="left:490px;top:1330px;width:330px;height:320px;background:linear-gradient(135deg,#f4f4f4,#cfcfcf)" role="img" aria-label="店舗内装の線画スケッチ"></div>

<!-- maintenance -->
<h2 class="abs sec-head" style="top:1740px"><i style="background:var(--blue)"></i>店舗リフォーム ✕ <em style="color:var(--blue)">アフターメンテナンス</em></h2>
<p class="abs lead serif" style="top:1840px;color:var(--blue)">リフォーム後のメンテナンスもお任せください。</p>
<div class="ph" style="left:72px;top:1910px;width:360px;height:250px;background:linear-gradient(135deg,#6d5a45,#d2c3a8)" role="img" aria-label="改装後の飲食店フロア写真"></div>
<p class="abs para" style="left:460px;top:1910px;width:360px">オープン後も定期的に点検を行い、設備の不具合や気になる箇所にすぐ対応いたします。長く快適にご利用いただけるよう、清掃や補修のご相談も承ります。小さな修繕から追加の改装まで、店舗の成長に合わせたサポートをお約束します。安心して営業に集中できる環境をご提供します。</p>

<!-- works -->
<h2 class="abs serif" style="left:72px;top:2200px;width:748px;font-size:20px;font-weight:400;border-bottom:1px solid var(--line);padding-bottom:8px">施工事例</h2>
<div class="ph" style="left:72px;top:2268px;width:348px;height:232px;background:linear-gradient(135deg,#3a2418,#c08a55)" role="img" aria-label="カフェバーの施工事例写真"></div>
<div class="ph" style="left:472px;top:2268px;width:348px;height:232px;background:linear-gradient(135deg,#5a3a22,#e0b27a)" role="img" aria-label="和食レストランの施工事例写真"></div>
<div class="abs work-cap" style="left:72px;top:2512px"><i class="chip">施工事例</i><span>カフェバー</span></div>
<div class="abs work-cap" style="left:472px;top:2512px"><i class="chip">施工事例</i><span>和食レストラン</span></div>
<div class="ph" style="left:72px;top:2572px;width:348px;height:232px;background:linear-gradient(135deg,#4d4038,#b7a592)" role="img" aria-label="居酒屋の施工事例写真"></div>
<div class="ph" style="left:472px;top:2572px;width:348px;height:232px;background:linear-gradient(135deg,#6a4a33,#dcc2a0)" role="img" aria-label="洋食レストランの施工事例写真"></div>
<div class="abs work-cap" style="left:72px;top:2816px"><i class="chip">施工事例</i><span>居酒屋</span></div>
<div class="abs work-cap" style="left:472px;top:2816px"><i class="chip">施工事例</i><span>洋食レストラン</span></div>

<!-- news -->
<h2 class="abs serif" style="left:72px;top:2930px;width:748px;font-size:20px;font-weight:400;border-bottom:1px solid var(--line);padding-bottom:8px">新着情報</h2>
<ul class="abs news">
  <li><i></i>2016/06/16<span>[店舗リフォーム事例] 宇都宮市</span></li>
  <li><i></i>2016/06/16<span>[店舗リフォーム事例] 宇都宮市</span></li>
  <li><i></i>2016/06/16<span>[店舗リフォーム事例] 宇都宮市</span></li>
</ul>

<!-- sidebar -->
<aside>
  <div class="abs side access">
    <h3>ACCESS</h3>
    <p class="big">店舗リフォームのミナト<br>(有限会社ミナト建設)</p>
    <p>〒321-0000<br>栃木県みどり市青葉町1-2-3</p>
    <p style="margin-top:10px;text-align:center">お問い合わせはこちらまで</p>
    <p class="ph-num">028-000-4172</p>
  </div>
  <div class="abs side" style="top:1050px">
    <div class="side-h" style="background:#8a6b4a">リフォーム施工事例</div>
    <ul class="case-list">
      <li><div role="img" aria-label="施工事例の小写真"></div>イタリアンレストラン</li>
      <li><div role="img" aria-label="施工事例の小写真"></div>イタリアンレストラン</li>
      <li><div role="img" aria-label="施工事例の小写真"></div>イタリアンレストラン</li>
      <li><div role="img" aria-label="施工事例の小写真"></div>イタリアンレストラン</li>
      <li style="border:0"><div role="img" aria-label="施工事例の小写真"></div>イタリアンレストラン</li>
    </ul>
  </div>
  <div class="abs side" style="top:1390px">
    <div class="side-h" style="background:var(--olive)">リフォーム関連ニュース</div>
    <ul class="news-side" style="list-style:none">
      <li><div role="img" aria-label="ニュース用の画像"></div>リフォーム関連記事</li>
      <li><div role="img" aria-label="ニュース用の画像"></div>リフォーム関連記事</li>
    </ul>
  </div>
  <div class="abs side" style="top:1660px">
    <div style="font-size:12px;border-bottom:1px solid var(--line);padding-bottom:6px;margin-bottom:10px">◆ 取り扱いメーカー</div>
    <div class="badge"></div>
    <div class="badge" style="margin-top:8px"></div>
  </div>
  <div class="abs side" style="top:1860px;height:120px;background:var(--olive);color:#fff;font-size:13px;padding:24px 20px">施工事例</div>
</aside>

<div class="abs pagetop">PAGETOP</div>
<footer>
  <div class="abs footer"></div>
  <svg class="abs" style="left:0;top:3160px" width="1200" height="280" aria-hidden="true">
    <polygon points="0,30 1200,0 1200,40 0,70" fill="#ffffff"/>
    <polygon points="0,70 1200,40 1200,56 0,86" fill="#6b4a3c"/>
  </svg>
  <div class="abs fnav"><span>リフォームとは</span><span>リフォーム工程</span><span>事例紹介</span><span>会社概要</span><span>お問合せ</span></div>
  <div class="abs flogo">
    <div class="n"><span style="font-size:12px">店舗リフォームの</span><b>ミナト</b></div>
    <span class="box">(有限会社ミナト建設)</span>
    <p>〒321-0000<br>栃木県みどり市青葉町1-2-3</p>
    <span class="num">028-000-4172</span>
  </div>
</footer>

</body>
</html>
```